Business Card Design Project 4 Construction Business

I am after a creative, but sleek and simple/ clean business card design. This design will form the basis of future items and might include a logo or simply a creative way to lay out the text of my company name 'keldmoor builds'
I like the simplicity of black and white however I would also be happy to see a splash of colour introduced somehow to give the text some interest and make it stand out.
I would like a double sided card.
I am young (ish!) and professional, offering construction and project management services, what I don't want is the traditional builders type card featuring a cheesy hammer/ saw image etc.
As the company name, keldmoor builds, suggests, we focus on working closely and collaboratively together, in synergy with all stakeholders involved in the projects that we undertake
Industry/Entity Type
Construction

```html
<!DOCTYPE html>
<html lang="en">
<head>
<meta charset="utf-8">
<title>Keldmoor Builds — Business Card</title>
<link href="https://fonts.googleapis.com/css2?family=Aldrich&display=swap" rel="stylesheet">
<style>
  :root {
    --backdrop: #f2f2f2;
    --card: #ffffff;
    --teal: #00b4cc;
    --ink: #0a0a0a;
  }
  * { margin: 0; padding: 0; box-sizing: border-box; }
  html, body {
    width: 1200px;
    height: 900px;
    overflow: hidden;
    background: var(--backdrop);
    font-family: "Aldrich", sans-serif;
  }
  .stage { position: relative; width: 1200px; height: 900px; }
  .card {
    position: absolute;
    left: 311px;
    width: 579px;
    height: 354px;
    background: var(--card);
  }
  .card--front { top: 50px; }
  .card--back { top: 496px; }

  .brand {
    position: absolute;
    inset: 0;
    display: flex;
    flex-direction: column;
    align-items: center;
    justify-content: center;
    gap: 22px;
  }
  .brand__mark {
    width: 34px;
    height: 34px;
    background: var(--teal);
  }
  .brand__name {
    color: var(--teal);
    font-size: 30px;
    letter-spacing: 1px;
    text-transform: uppercase;
    text-align: center;
  }

  .holder {
    position: absolute;
    top: 50px;
    right: 132px;
    text-align: right;
  }
  .holder__name {
    color: var(--ink);
    font-size: 24px;
    letter-spacing: 0.5px;
    line-height: 1.2;
  }
  .holder__role {
    color: var(--teal);
    font-size: 18px;
    line-height: 1.3;
  }
  .holder-mark {
    position: absolute;
    top: 50px;
    left: 462px;
  }

  .contact {
    position: absolute;
    left: 55px;
    font-size: 16px;
    letter-spacing: 0.6px;
    line-height: 24px;
  }
  .contact--address { top: 163px; }
  .contact--reach { top: 270px; line-height: 23px; }
  .label { color: var(--ink); }
  .value { color: var(--teal); }
  .value--dark { color: var(--ink); }
</style>
</head>
<body>
<main class="stage">
  <section class="card card--front" aria-label="Card front">
    <div class="brand">
      <span class="brand__mark" aria-hidden="true"></span>
      <p class="brand__name">Keldmoor Builds</p>
    </div>
  </section>

  <section class="card card--back" aria-label="Card back">
    <div class="holder">
      <p class="holder__name">Oliver Brant</p>
      <p class="holder__role">Director</p>
    </div>
    <svg class="holder-mark" width="60" height="60" viewBox="0 0 60 60" aria-hidden="true">
      <circle cx="30" cy="30" r="28" fill="none" stroke="var(--teal)" stroke-width="3"/>
    </svg>

    <div class="contact contact--address">
      <p class="label">address:</p>
      <p class="value">14 Harlow St</p>
      <p class="value">Kirrawee NSW 2232</p>
    </div>

    <div class="contact contact--reach">
      <p><span class="label">ph: </span><span class="value--dark">0400 555 128</span></p>
      <p class="value">e: oliver@keldmoorbuildsgroup.com.au</p>
    </div>
  </section>
</main>
</body>
</html>
```